Refresh of a rather different IT outfit website

Our web site is starting to show it's age. You can see the existing site here: www.plumbcorner.net. As a growing company we want to come across as a dynamic collection of IT experts.

We want to update the design so are open to any colour palette and look, but want to retain our current table logo. We use the logo on our business cards but with a white background - see the attached file, so you don't need to keep the brown or the green.

The design should consider the range of browsers that will be looking at the site - so please show how it will look on a wide screen laptop and a 768x1024 tablet.

We want to add some pages about our team and their skills, probably with photos of each person on the team.

This is an uncoded project - the PSD files of the design is required, not coding.
Updates

Thanks everyone for the submissions so far.  It's a holiday day in the UK today but we will get some feedback on the designs so far out to you.

Target Market(s)

Architects and other creative types looking for IT support

Industry/Entity Type

Business

Font styles to use
Serif
Sans Serif

Requirements
Must have
• Must look good on a laptop and an iPad.

```html
<!DOCTYPE html>
<html lang="en">
<head>
<meta charset="utf-8">
<title>plumbcorner – Serious IT Support for business</title>
<link rel="stylesheet" href="https://fonts.googleapis.com/css2?family=Montserrat:wght@400;500;600&family=Arimo:wght@400;700&display=swap">
<style>
:root{
  --brand:#9a1350;
  --cyan:#2fb4cb;
  --cyan-dark:#1e8fa3;
  --green:#4fcea3;
  --orange:#e8a447;
  --red:#ec6a6a;
  --purple:#a87adb;
  --gold:#d8a51a;
  --ink:#1c1c1c;
  --paper:#f2f2f2;
  --partners:#333333;
  --footer:#222222;
  --white:#ffffff;
}
*{margin:0;padding:0;box-sizing:border-box}
html,body{width:1200px;height:2764px;overflow:hidden}
body{font-family:"Arimo",Arial,sans-serif;color:var(--ink);background:var(--white)}
.page{position:relative;width:1200px;height:2764px}

.site-header{height:108px;background:var(--brand);display:flex;align-items:center;padding:0 161px}
.brand{display:flex;align-items:center;gap:14px;color:var(--white);font-family:"Montserrat",sans-serif;font-weight:500;font-size:36px;letter-spacing:.5px}
.brand-mark{width:26px;height:26px;background:var(--white)}
.main-nav{margin-left:auto;display:flex;gap:22px;margin-right:-100px}
.main-nav a{color:var(--white);text-decoration:none;font-size:17px}

.hero{position:relative;height:516px;background:linear-gradient(#f4f4f4,#ffffff)}
.hero-art{position:absolute;left:92px;top:30px;width:1060px;height:290px;background:linear-gradient(90deg,#e9774a 0%,#f0a33a 30%,#3a86b8 60%,#2a6f9f 100%);opacity:.85;border-radius:4px}
.hero-copy{position:absolute;left:0;right:0;top:300px;height:216px;text-align:center;padding-top:110px;background:linear-gradient(rgba(255,255,255,0),rgba(255,255,255,.9) 30%,#fff 60%)}
.hero h1{position:absolute;left:0;right:0;top:10px;font-family:"Montserrat",sans-serif;font-weight:500;font-size:60px;line-height:70px;color:#111;letter-spacing:-.5px;white-space:nowrap}
.hero p{width:860px;margin:0 auto;font-size:21px;line-height:30px;color:#111}

.services-intro{position:relative;height:417px;background:var(--cyan)}
.services-intro h2{position:absolute;left:0;right:0;top:60px;text-align:center;font-family:"Montserrat",sans-serif;font-weight:600;font-size:60px;line-height:72px;color:var(--white);letter-spacing:-.5px;white-space:nowrap}
.intro-rule{position:absolute;left:177px;top:175px}

.service{display:flex;align-items:center;height:211px;color:var(--white)}
.service.first{position:absolute;left:0;top:240px;height:150px;width:1200px}
.service-title{width:543px;text-align:right;font-family:"Montserrat",sans-serif;font-weight:500;font-size:38px;line-height:48px}
.service-list{list-style:none;margin-left:53px;font-size:17px;line-height:22px;color:#1a1a1a}
.cloud{background:var(--green)}
.recovery{background:var(--orange)}
.virtual{background:var(--red)}
.cad{background:var(--purple)}

.updates{position:relative;height:647px;background:var(--paper)}
.update-column{position:absolute;top:105px;width:410px}
.update-column.news{left:159px}
.update-column.articles{left:654px}
.update-column h2{font-family:"Montserrat",sans-serif;font-weight:500;font-size:40px;line-height:50px;color:var(--gold);margin-bottom:20px}
.post h3{font-size:14px;font-weight:700;color:var(--brand);margin-bottom:16px;white-space:nowrap}
.post p{font-size:14px;line-height:18px;margin-bottom:16px}
.post{margin-bottom:26px}
.more{position:absolute;right:0;top:472px;font-size:14px;color:var(--brand);text-decoration:none}

.partners{height:166px;background:var(--partners);display:flex;align-items:center;justify-content:center;gap:62px}
.partner{display:flex;align-items:center;gap:10px;color:#e6e6e6;font-weight:700;font-size:24px}
.partner-dot{width:22px;height:22px;border-radius:50%;background:#e6e6e6}

.site-footer{height:65px;background:var(--footer);display:flex;align-items:center;padding:0 110px;color:#dddddd;font-size:12px}
.footer-nav a{color:#dddddd;text-decoration:none}
.copyright{margin-left:auto}
</style>
</head>
<body>
<div class="page">
  <header class="site-header">
    <div class="brand"><span class="brand-mark"></span>plumbcorner</div>
    <nav class="main-nav">
      <a href="#">Home</a><a href="#">About Us</a><a href="#">What we do</a><a href="#">News Blog</a><a href="#">Articles</a><a href="#">Clients</a><a href="#">Partners</a>
    </nav>
  </header>

  <section class="hero">
    <div class="hero-art" role="img" aria-label="Illustration of flat IT and business icons: charts, gears, calendar, cloud, globe and devices"></div>
    <div class="hero-copy">
      <h1>Serious IT Support for business</h1>
      <p>Plumbcorner was established with a specific aim: to consistently deliver an advanced and comprehensive IT service for ambitious growing companies across all industry sectors.</p>
    </div>
  </section>

  <section class="services-intro">
    <h2>What you get from plumbcorner</h2>
    <svg class="intro-rule" width="820" height="30" viewBox="0 0 820 30">
      <line x1="0" y1="1" x2="820" y2="1" stroke="#1e8fa3" stroke-width="2"/>
      <polygon points="376,1 422,1 399,24" fill="#1e8fa3"/>
    </svg>
    <div class="service first">
      <h3 class="service-title">IT Support &amp;<br>Management</h3>
      <ul class="service-list">
        <li>Client / Server Networks</li><li>Cabling and Wireless Solutions</li><li>Data and Voice Convergence</li><li>Security and Penetration Testing</li><li>Multi-site Connectivity</li>
      </ul>
    </div>
  </section>

  <section class="service cloud">
    <h3 class="service-title">Cloud<br>Computing</h3>
    <ul class="service-list">
      <li>Custom Control Panel Manages Resources</li><li>Increase Performance and Availability</li><li>Unlimited Bandwidth/Unlimited Storage</li><li>Geographic Separation for Failover</li><li>Transfer of Risk &amp; Reduced TCO</li>
    </ul>
  </section>
  <section class="service recovery">
    <h3 class="service-title">Disaster<br>Recovery</h3>
    <ul class="service-list">
      <li>Defined RPO and RTO objectives</li><li>Enterprise Class Recoverability</li><li>Mirrored Off-site Servers/Data</li><li>Rapid Deployment of Failover Infrastructure</li><li>Low Incremental Costs</li>
    </ul>
  </section>
  <section class="service virtual">
    <h3 class="service-title">Virtualisation</h3>
    <ul class="service-list">
      <li>Server and Storage Virtualisation</li><li>High Availability Server Nodes</li><li>Application Streaming</li><li>Secure Remote Desktops</li><li>Xenline and VirtuMesh Deployments</li>
    </ul>
  </section>
  <section class="service cad">
    <h3 class="service-title">CAD<br>Services</h3>
    <ul class="service-list">
      <li>Corbel Product Customisation</li><li>CAD Management</li><li>BIM for Designers</li><li>Draftwell FORMA Consultancy</li><li>Training and Implementation</li>
    </ul>
  </section>

  <section class="updates">
    <div class="update-column news">
      <h2>Latest News</h2>
      <article class="post">
        <h3>Plumbcorner Fonephone and Robodroid App launched</h3>
        <p>Plumbcorner have released Fonephone and Robodroid apps that allow customers to submit and track support requests on their smart phones.</p>
        <p>You can find the Fonephone version on TuneStore here and the Robodroid version in the Robodroid Market here</p>
      </article>
      <article class="post">
        <h3>Plumbcorner Fonephone and Robodroid App launched</h3>
        <p>Plumbcorner have released Fonephone and Robodroid apps that allow customers to submit and track support requests on their smart phones.</p>
        <p>You can find the Fonephone version on TuneStore here and the Robodroid version in the Robodroid Market here</p>
      </article>
      <a class="more" href="#">more...</a>
    </div>
    <div class="update-column articles">
      <h2>Latest Articles</h2>
      <article class="post">
        <h3>Plumbcorner Fonephone and Robodroid App launched</h3>
        <p>Plumbcorner have released Fonephone and Robodroid apps that allow customers to submit and track support requests on their smart phones.</p>
        <p>You can find the Fonephone version on TuneStore here and the Robodroid version in the Robodroid Market here</p>
      </article>
      <article class="post">
        <h3>Plumbcorner Fonephone and Robodroid App launched</h3>
        <p>Plumbcorner have released Fonephone and Robodroid apps that allow customers to submit and track support requests on their smart phones.</p>
        <p>You can find the Fonephone version on TuneStore here and the Robodroid version in the Robodroid Market here</p>
      </article>
      <a class="more" href="#">more...</a>
    </div>
  </section>

  <section class="partners">
    <span class="partner"><span class="partner-dot"></span>Boxwell</span>
    <span class="partner"><span class="partner-dot"></span>Mailsafe</span>
    <span class="partner">Pixelform</span>
    <span class="partner"><span class="partner-dot"></span>Gatekeep</span>
    <span class="partner">Sentrix</span>
    <span class="partner">Netwise</span>
  </section>

  <footer class="site-footer">
    <nav class="footer-nav"><a href="#">Home</a> | <a href="#">About Us</a> | <a href="#">What we do</a> | <a href="#">News Blog</a> | <a href="#">Articles</a> | <a href="#">Clients</a> | <a href="#">Partners</a></nav>
    <span class="copyright">Copyright 2014. All Rights Reserved</span>
  </footer>
</div>
</body>
</html>
```